Business Card Design Project for Electrical Company

We need a business card designed for a new Electrical Company called Venrol Electrical Solutions, i dont mind if only Venrol Electrical is used. We are a domestic and commercial Electrical Company that provides a range of Electrical Services. Our Company colours are Fluro Yellow and Black with the Lightning bolt picture attached.I have attached a card that has been made i think it is rather basic and am looking for something more. the font of Venrol Electrical has been used on our car graphics as well as the lightning bolt. i want to keep them the same so we can brand our business. Some things we want on the front of the card are Venrol Electrical Solutions, Derek Pollard, 0438562917, admin@venrolelectrical.example, Lic No 58342, Servicing CQ Region. But we want Dereks name seperate to the phone number as its the phone number for the office, derek wont be answering the phone so we are thinking we dont want to give that impression. What do you think? with all that if you have complete different font designs please submit what you think would work best. keeping in mind our company name and details as well as coulors.

Industry/Entity Type

Business

```html
<!DOCTYPE html>
<html lang="en">
<head>
<meta charset="utf-8">
<title>Venrol Electrical Solutions – Business Card</title>
<link rel="stylesheet" href="https://fonts.googleapis.com/css2?family=Arimo:wght@400;700&display=swap">
<style>
  :root {
    --fluro: #c6d92a;
    --fluro-square: #a9c93a;
    --ink: #111111;
    --paper: #ffffff;
    --stage: #e9e9e9;
    --grey-text: #bdbdbd;
    --body-text: #2a2a2a;
    --bolt-dark: #6a6a6a;
    --bolt-light: #f4f4f4;
  }
  * { box-sizing: border-box; margin: 0; padding: 0; }
  html, body {
    width: 1200px; height: 900px; overflow: hidden;
    background: var(--stage);
    font-family: "Arimo", Arial, sans-serif;
  }
  .canvas {
    position: relative; width: 1200px; height: 900px;
  }
  .card {
    position: absolute; left: 280px;
    width: 640px; height: 366px;
    background: var(--paper);
    overflow: hidden;
    box-shadow: 0 10px 28px rgba(0,0,0,.22);
  }
  .card--back { top: 54px; }
  .card--front { top: 480px; }

  /* back */
  .bolt-art {
    position: absolute; left: 0; top: 0;
    width: 330px; height: 366px;
    background: linear-gradient(115deg, var(--bolt-light) 0%, #d9d9d9 30%, var(--bolt-light) 55%, var(--paper) 100%);
  }
  .services {
    position: absolute; right: 34px; top: 58px;
    list-style: none; text-align: right;
  }
  .services li {
    display: flex; justify-content: flex-end; align-items: center;
    gap: 12px; height: 31px;
    font-size: 17px; color: var(--body-text);
  }
  .services li::after {
    content: ""; width: 11px; height: 11px;
    background: var(--fluro-square);
    box-shadow: inset 0 0 0 1px rgba(0,0,0,.12);
  }

  /* front */
  .front-band {
    position: absolute; left: 0; bottom: 0; width: 100%; height: 166px;
    background: var(--ink);
    border-top: 5px solid var(--fluro);
  }
  .front-wedge { position: absolute; left: 0; top: 0; }
  .brand {
    position: absolute; left: 250px; top: 58px; width: 360px;
    font-weight: 700; color: var(--ink);
    font-size: 40px; line-height: 1.02; letter-spacing: .5px;
    text-transform: uppercase;
  }
  .brand__sub { display: block; font-size: 40px; }
  .person {
    position: absolute; left: 34px; bottom: 50px;
  }
  .person__name { color: var(--paper); font-size: 19px; letter-spacing: 1px; text-transform: uppercase; }
  .person__role { color: var(--fluro); font-size: 13px; margin-top: 6px; }
  .person__licence { color: var(--grey-text); font-size: 13px; margin-top: 10px; }
  .divider {
    position: absolute; left: 300px; bottom: 26px;
    width: 1px; height: 110px; background: #444;
  }
  .contacts {
    position: absolute; left: 330px; bottom: 40px; list-style: none;
  }
  .contacts li {
    display: flex; align-items: center; gap: 12px;
    color: var(--paper); font-size: 15px; height: 28px;
  }
  .contacts svg { width: 14px; height: 14px; flex: none; }
</style>
</head>
<body>
<main class="canvas">

  <section class="card card--back" aria-label="Business card back">
    <div class="bolt-art" role="img" aria-label="Lightning bolt illustration branching across the left side"></div>
    <ul class="services">
      <li>Light &amp; Power</li>
      <li>TV &amp; Data</li>
      <li>Test &amp; Tagging</li>
      <li>Renovations</li>
      <li>Design &amp; Installation</li>
      <li>Air Con Installation</li>
      <li>Smoke Detectors</li>
      <li>Residential</li>
    </ul>
  </section>

  <section class="card card--front" aria-label="Business card front">
    <svg class="front-wedge" width="200" height="200" viewBox="0 0 200 200" aria-hidden="true">
      <polygon points="0,0 0,195 110,195" fill="var(--ink)"/>
      <line x1="0" y1="0" x2="112" y2="197" stroke="var(--fluro)" stroke-width="5"/>
    </svg>
    <h1 class="brand">Venrol Electrical<span class="brand__sub">Solutions</span></h1>
    <div class="front-band"></div>

    <div class="person">
      <p class="person__name">Derek Pollard</p>
      <p class="person__role">President &amp; CEO</p>
      <p class="person__licence">Lic No 58342, Servicing CQ Region</p>
    </div>

    <span class="divider"></span>

    <ul class="contacts">
      <li>
        <svg viewBox="0 0 14 14" aria-hidden="true"><path d="M3 1h3l1 3-2 1a7 7 0 0 0 4 4l1-2 3 1v3c0 1-1 1-2 1A11 11 0 0 1 1 3c0-1 1-2 2-2z" fill="var(--fluro)"/></svg>
        0438.562.917
      </li>
      <li>
        <svg viewBox="0 0 14 14" aria-hidden="true"><rect x="1" y="3" width="12" height="8" fill="var(--fluro)"/><path d="M1 3l6 5 6-5" stroke="var(--ink)" fill="none"/></svg>
        admin@venrolelectrical.example
      </li>
      <li>
        <svg viewBox="0 0 14 14" aria-hidden="true"><circle cx="7" cy="7" r="6" fill="var(--fluro)"/><path d="M1 7h12M7 1c-3 3-3 9 0 12M7 1c3 3 3 9 0 12" stroke="var(--ink)" fill="none"/></svg>
        www.venrolelectrical.example
      </li>
    </ul>
  </section>

</main>
</body>
</html>
```